Real Estate "For Sale" Sign for construction company

We need a sign that we can use to hang on a post and place on the road when we sell a property. The sign will be simple and will need to mainly feature our logo (files attached), as well as the words "For Sale", and then our phone number "(555) 617 3489". The sign will hang on a post that'll look something like the attached picture.

Target Market(s)

Home buyers

Industry/Entity Type

Real Estate

Font styles to use
Serif
Sans Serif

Colors
0054AA
0677BA
7BADD7
CADEEF
E8F1F8
0094D4
00A9DD
6FCCEA
C7EBF8
E9F6FB

Requirements
Must have
• For Sale & our phone number

```html
<!DOCTYPE html>
<html lang="en">
<head>
<meta charset="UTF-8">
<title>For Sale Sign</title>
<link rel="stylesheet" href="https://fonts.googleapis.com/css2?family=Poppins:wght@400;700&display=swap">
<style>
  :root {
    --page-bg: #ececec;
    --sign-sky: #92d8f6;
    --sign-navy: #2e3555;
    --brand-blue: #2e79c2;
    --white: #ffffff;
  }
  * { margin: 0; padding: 0; box-sizing: border-box; }
  html, body {
    width: 1200px;
    height: 1096px;
    overflow: hidden;
    background: var(--page-bg);
  }
  .sign {
    position: absolute;
    left: 40px;
    top: 68px;
    width: 1120px;
    height: 960px;
    background: var(--sign-sky);
  }
  .headline {
    position: absolute;
    top: 36px;
    left: 0;
    right: 0;
    text-align: center;
    font-family: "Poppins", sans-serif;
    font-weight: 700;
    font-size: 230px;
    line-height: 1.2;
    letter-spacing: -3px;
    color: var(--sign-navy);
    white-space: nowrap;
  }
  .brand {
    position: absolute;
    top: 330px;
    left: 0;
    right: 0;
    display: flex;
    flex-direction: column;
    align-items: center;
  }
  .brand-mark {
    width: 170px;
    height: 170px;
    border-radius: 50%;
    background: var(--brand-blue);
  }
  .brand-name {
    margin-top: 18px;
    font-family: "Poppins", sans-serif;
    font-weight: 400;
    font-size: 88px;
    line-height: 1;
    color: var(--brand-blue);
    white-space: nowrap;
  }
  .brand-sub {
    margin-top: 16px;
    font-family: "Poppins", sans-serif;
    font-weight: 400;
    font-size: 26px;
    line-height: 1;
    letter-spacing: 24px;
    padding-left: 24px;
    color: var(--brand-blue);
  }
  .contact-band {
    position: absolute;
    left: 0;
    right: 0;
    bottom: 0;
    height: 236px;
    background: var(--sign-navy);
    display: flex;
    align-items: center;
    justify-content: center;
  }
  .phone {
    font-family: "Poppins", sans-serif;
    font-weight: 700;
    font-size: 132px;
    line-height: 1;
    letter-spacing: -2px;
    color: var(--white);
    padding-top: 8px;
    white-space: nowrap;
  }
</style>
</head>
<body>
  <div class="sign">
    <h1 class="headline">FOR SALE</h1>
    <div class="brand">
      <span class="brand-mark"></span>
      <span class="brand-name">Ridgeline Oak</span>
      <span class="brand-sub">PROPERTIES</span>
    </div>
    <div class="contact-band">
      <p class="phone">(555) 617 3489</p>
    </div>
  </div>
</body>
</html>
```